Online Music Gear Store needs Business Cards

We need BC designs for our e-commerce for meetings and networking
we are an Online Store and we sell Audio and Music Equipment and Gear
we also provide EVENTUAL Audio and Music Production services but our core service is the Online Store: Selling Premium Brands

we are based in Tijuana and San Diego CA.
our brand/name is: Vellmoor

our name comes from the early tape machines that the Corvanes and many other early day artist used to record with to do their magnificent masterpieces.

Now in 2014 we can have Amazing Studio-Quality Multitrack sessions with a few pieces of Gear and an Slatepod... For example, you can only have your Pocketline and an Brisa Tandem to start recording using Loft Deck for Quorix.

If the best bands from the early days had to use million dollar recording studios with very expensive gear such as 4-track tape machines... now you can achieve better sounding results in your bedroom, using the gear we sell.

Thats what we try to Communicate with the Name:

That you... a young musician can start doing multitrack sessions using the Best Gear with the Latest Technology and compatible with Trelons, Quorix devices:

Example of the Premium Brands we sell are:
Brisa, ZQ Mediaworks

we want to communicate (even if we are an ecommerce and a startup) that we are Serious, and Very Elegant, Sophisticated and Minimal.

that we provide Complete solutions, the best gear... the best brands... that we also do our productions with the best gear, best brands and very important we are Pomeroy ONLY, Trelons Only

examples of the brands we sell are Kolbrandt, Brisa, ZQ Mediaworks, Rolf Ingham Instruments, Arc 9. Our focus is Music Technology.
we also use Cadence Max Q.

Our favorite colors are black, white, grey, silver, orange, blue, green, maybe bit of yellow.

No need to use all of them but you can combine. At the end you can use Color Theory to achieve assertive communication.

Target Market(s)

CEO's, VP's, VC's, Sales People, High Class executives...
Purchasing Departments, and Corporations.

Industry/Entity Type

E-Commerce

Requirements
Must have
• Should include:

1. Logo
2. website,
3. Managing Director Info:
4. Minimal and Elegant/Upper Class

feel free to suggest ideas, feel free to play around with logo and fonts as well... since we are not 100% happy with our logo...

must also show that we are Pomeroy and Trelon only in a way without being obvious or without showing Pomeroy Logo

we need to have at the end of the project the .AI
.PSD and any related designed file to edit in the future, logo, numbers, etc...

my info:

Tomas Emil Varga-Lindqvist
Vellmoor | Valdoria, Puerto Serran, Costa Linde,
Chatterbox | Peeplo | Zenbo+ | Clipwall | Snapframe ???? (what do you thing about this links ???) too much ???
Mobile: +5219987350418 | 0115219987350418
USA Number: 1-800-572-9183
VuCall & QuickNote: studio@vellmoor-example.mx
Talkwave: studiovellmoormx
Should not have
• it shouldn't use our real address, but should imply that we are in Mexico City, in Tijuana and San Diego CA.

Should not use the Pomeroy Logo (even if we are Pomeroy only)

should not have Robotix or PC/Panelix related designs.

```html
<!DOCTYPE html>
<html lang="en">
<head>
<meta charset="utf-8">
<title>Vellmoor Business Card</title>
<link rel="stylesheet" href="https://fonts.googleapis.com/css2?family=Questrial&display=swap">
<style>
  :root {
    --backdrop: #cfcfcd;
    --card-black: #111111;
    --card-white: #ffffff;
    --ink: #111111;
    --ink-light: #ffffff;
    --name-green: #217a1f;
    --brand-green: #4cc93a;
    --detail-grey: #8a8a8a;
    --accent-blue: #23a8cc;
  }
  * { margin: 0; padding: 0; box-sizing: border-box; }
  html, body {
    width: 1200px;
    height: 728px;
    overflow: hidden;
    background: var(--backdrop);
    font-family: "Questrial", "Century Gothic", sans-serif;
  }
  .canvas { position: relative; width: 1200px; height: 728px; }

  .card {
    position: absolute;
    border-radius: 24px;
    overflow: hidden;
  }

  /* Front */
  .card-front {
    left: 142px; top: 119px;
    width: 409px; height: 251px;
    background: var(--card-black);
  }
  .front-mark {
    position: absolute;
    left: 50%; top: 56px;
    transform: translateX(-50%);
    display: flex; flex-direction: column; align-items: center;
  }
  .brand-dot {
    display: block;
    border-radius: 50%;
    background: var(--brand-green);
  }
  .front-mark .brand-dot { width: 84px; height: 84px; }
  .front-mark .brand-name {
    margin-top: 36px;
    font-size: 27px;
    line-height: 1;
    color: var(--ink-light);
    white-space: nowrap;
  }

  /* Back */
  .card-back {
    left: 641px; top: 285px;
    width: 410px; height: 250px;
    background: var(--card-white);
  }
  .back-mark {
    position: absolute;
    left: 22px; top: 66px;
    width: 112px;
    display: flex; flex-direction: column; align-items: center;
  }
  .back-mark .brand-dot { width: 62px; height: 62px; }
  .back-mark .brand-name {
    margin-top: 28px;
    font-size: 17px;
    line-height: 1;
    color: var(--ink);
    white-space: nowrap;
  }

  .holder-name {
    position: absolute;
    right: 26px; top: 28px;
    font-size: 19px;
    font-weight: 400;
    color: var(--name-green);
    white-space: nowrap;
  }
  .contact-list {
    position: absolute;
    right: 16px; top: 62px;
    list-style: none;
    text-align: right;
  }
  .contact-list li {
    display: flex; justify-content: flex-end; align-items: center;
    height: 24.5px;
    font-size: 12.5px;
    color: var(--detail-grey);
    white-space: nowrap;
  }
  .contact-list li.gap { margin-top: 16px; }
  .contact-list svg { width: 11px; height: 11px; margin-left: 10px; fill: var(--accent-blue); flex: none; }

  .web-band {
    position: absolute;
    left: 0; bottom: 0;
    width: 100%; height: 38px;
    background: var(--accent-blue);
    color: var(--ink-light);
    font-size: 13px;
    display: flex; align-items: center; justify-content: center;
  }
</style>
</head>
<body>
<main class="canvas">

  <section class="card card-front" aria-label="Card front">
    <div class="front-mark">
      <span class="brand-dot"></span>
      <span class="brand-name">Vellmoor.mx</span>
    </div>
  </section>

  <section class="card card-back" aria-label="Card back">
    <div class="back-mark">
      <span class="brand-dot"></span>
      <span class="brand-name">Vellmoor.mx</span>
    </div>

    <h1 class="holder-name">Tomas Emil Varga-Lindqvist</h1>

    <ul class="contact-list">
      <li>Valdoria, Puerto Serran, Costa Linde
        <svg viewBox="0 0 12 12"><path d="M6 0.5C3.8 0.5 2.2 2.1 2.2 4.2 2.2 7 6 11.5 6 11.5S9.8 7 9.8 4.2C9.8 2.1 8.2 0.5 6 0.5Zm0 5.2a1.5 1.5 0 1 1 0-3 1.5 1.5 0 0 1 0 3Z"/></svg>
      </li>
      <li>+5219987350418 0115219987350418
        <svg viewBox="0 0 12 12"><path d="M3 0.5h6a1 1 0 0 1 1 1v9a1 1 0 0 1-1 1H3a1 1 0 0 1-1-1v-9a1 1 0 0 1 1-1Zm0.6 1.4v6.6h4.8V1.9Z"/></svg>
      </li>
      <li>1-800-572-9183
        <svg viewBox="0 0 12 12"><path d="M1 4.2C1 2.5 3.2 1.5 6 1.5S11 2.5 11 4.2L9 5 8.3 3.8H3.7L3 5ZM2.5 6.2h7l1 4.3h-9Z"/></svg>
      </li>
      <li class="gap">studio@vellmoor-example.mx
        <svg viewBox="0 0 12 12"><circle cx="6" cy="6" r="5.5"/></svg>
      </li>
      <li>studiovellmoormx
        <svg viewBox="0 0 12 12"><rect x="0.5" y="0.5" width="11" height="11" rx="1"/></svg>
      </li>
    </ul>

    <div class="web-band">http://www.vellmoor-example.mx</div>
  </section>

</main>
</body>
</html>
```